Tarnwick Growth Systems Wordpress Design

We need a design for a company that focuses on Data Driven Marketing Technology Solutions. We have an existing web site (www.tarnwickgrowsys.example) that needs to be totally replaced. I want to keep certain elements of the site layout (e.g. menus, menu bar email signup), but I don't like the content in the sliders (sliders are not a requirement). I want to keep the blog, but again want a more professional looking presentation for the blog. I also want to add my twitter feed to the home page. I also want to create a professional pages that better articulates what we do from a services perspective. Web site should use colors from the attached logo although I'm open to a different color palate. Web site should communicate a data and technology focus on marketing and customer engagement. From a design perspective I want this to be extensible (e.g. standard WP plugins) and I really want a clean, simple, well performing CSS scheme. I think we are talking about 4 pages here. The pages would include a home page, a services pages (see attached), an About Me page, and a landing pages for email subscriptions. See http://plumelinestudio.example/ and http://www.quillharborworks.example/#who-is-quillharbor for an example of sites I like.

```html
<!DOCTYPE html>
<html lang="en">
<head>
<meta charset="utf-8">
<title>Tarnwick Growth Systems</title>
<link rel="stylesheet" href="https://fonts.googleapis.com/css2?family=Open+Sans:wght@400;600;700;800&display=swap">
<style>
:root{
  --orange:#ef9a1f;
  --orange-dark:#d5790f;
  --ink:#2b2b2b;
  --text:#666;
  --muted:#999;
  --line:#e2e2e2;
  --band:#ececec;
  --footer:#2e2e2e;
  --footer-deep:#242424;
  --white:#fff;
}
*{box-sizing:border-box;margin:0;padding:0}
html,body{width:706px;height:1200px;overflow:hidden;background:var(--white)}
body{font-family:"Open Sans",Arial,sans-serif;color:var(--text);font-size:7px;line-height:1.45}
.wrap{width:574px;margin:0 auto;position:relative}

/* header */
.site-header{height:86px}
.site-header .wrap{display:flex;align-items:center;justify-content:space-between;height:86px}
.brand{display:flex;align-items:center;gap:7px}
.brand-mark{width:20px;height:20px;border-radius:50%;background:var(--orange)}
.brand-name{font-size:12px;font-weight:700;color:var(--ink)}
.signup{display:flex;gap:6px}
.signup-input{width:104px;height:18px;border:1px solid #d6d6d6;font-size:6px;color:var(--muted);padding:4px 6px}
.signup-btn{width:62px;height:18px;background:#333;color:var(--white);font-size:6px;font-weight:700;text-align:center;line-height:18px;letter-spacing:.5px;border-radius:2px}

/* nav */
.main-nav{height:18px;background:linear-gradient(var(--orange),var(--orange-dark))}
.main-nav .wrap{display:flex;height:18px;align-items:center}
.nav-item{font-size:6px;font-weight:700;color:var(--white);padding:0 11px;height:18px;line-height:18px;letter-spacing:.4px}
.nav-item.active{background:#c66c08}
.nav-search{margin-left:auto;width:84px;height:12px;background:rgba(255,255,255,.25);border:1px solid rgba(255,255,255,.5);color:var(--white);font-size:5.5px;padding:1px 5px;display:flex;justify-content:space-between;align-items:center}

/* hero */
.hero{height:300px;background:linear-gradient(180deg,#cfe0ea 0%,#b9d0da 22%,#7f9a6e 45%,#5f7f4a 70%,#8a9a72 100%)}

/* main */
.content{height:485px;padding-top:32px}
.content .wrap{display:flex;justify-content:space-between}
.blog{width:358px}
.section-title{font-size:15px;font-weight:800;color:var(--ink);letter-spacing:.2px;margin-bottom:12px}
.post{display:flex;gap:12px;padding:10px 0 8px;border-bottom:1px solid var(--line);height:96px}
.post-thumb{width:88px;height:62px;flex:none}
.post-body{flex:1;display:flex;flex-direction:column}
.post-title{font-size:10px;font-weight:700;color:var(--ink);line-height:1.25;margin-bottom:4px}
.post-excerpt{font-size:5.5px;color:var(--muted);line-height:1.5}
.post-meta{margin-top:auto;display:flex;justify-content:space-between;font-size:5.5px;color:var(--muted)}
.read-more{color:var(--orange);font-weight:700}

.sidebar{width:142px}
.side-title{font-size:10px;font-weight:800;color:var(--ink);margin-bottom:8px}
.side-lead{font-size:6px;font-weight:700;color:var(--ink);margin-bottom:5px}
.side-text{font-size:5.5px;color:var(--muted);margin-bottom:6px;line-height:1.55}
.cta{display:block;background:var(--orange);color:var(--white);font-size:5.5px;font-weight:700;text-align:center;padding:6px 0;margin:10px 0 22px;letter-spacing:.3px}
.recent{display:flex;gap:7px;padding:6px 0;border-bottom:1px solid var(--line)}
.recent-thumb{width:40px;height:30px;flex:none}
.recent-text{font-size:5.5px;color:var(--ink);font-weight:600;line-height:1.4}
.recent-text span{display:block;color:var(--muted);font-weight:400}

.t1{background:linear-gradient(135deg,#dfe8ef,#b8c8d8 60%,#c24040)}
.t2{background:linear-gradient(135deg,#2a8fc8,#7cc3e6)}
.t3{background:linear-gradient(135deg,#e8eef3,#4a86c5)}
.t4{background:linear-gradient(180deg,#a9cbe6,#d8c9a8)}
.t5{background:linear-gradient(135deg,#c9c9c9,#8a8a8a)}

/* services band */
.band{height:179px;background:var(--band);padding-top:20px}
.band .wrap{display:flex;justify-content:space-between}
.band-title{font-size:7px;font-weight:800;color:var(--ink);margin-bottom:12px;letter-spacing:.3px}
.services{width:330px}
.service-grid{display:grid;grid-template-columns:1fr 1fr;gap:14px 16px}
.service{display:flex;gap:7px}
.service-thumb{width:50px;height:36px;flex:none}
.service-text{font-size:5.5px;color:var(--muted);line-height:1.45}
.service-text b{display:block;color:var(--ink);font-weight:700}
.tweets{width:210px}
.tweet{display:flex;gap:6px;margin-bottom:8px}
.tweet-icon{width:8px;height:8px;background:var(--orange);border-radius:50%;flex:none;margin-top:1px}
.tweet-text{font-size:5.5px;color:var(--text);line-height:1.45}
.tweet-text span{color:var(--orange)}
.tweet-text em{display:block;font-style:normal;color:var(--muted)}

/* footer */
.site-footer{height:150px;background:var(--footer)}
.site-footer .wrap{display:flex;height:95px;padding-top:18px}
.foot-brand{width:120px}
.foot-brand .brand-name{color:var(--white);font-size:9px}
.foot-brand p{font-size:5px;color:#9a9a9a;margin-top:6px;line-height:1.5}
.foot-links{display:flex;gap:26px;margin-left:16px}
.foot-col{font-size:5.5px;color:#bdbdbd;line-height:1.9}
.social{margin-left:auto;width:110px}
.social-title{font-size:6px;font-weight:700;color:var(--white);margin-bottom:8px;letter-spacing:.4px}
.social-row{display:flex;gap:5px}
.social-dot{width:13px;height:13px;border-radius:50%;background:#8a8a8a}
.social-dot.accent{background:var(--orange)}
.copyright{height:55px;background:var(--footer-deep);font-size:5px;color:#8a8a8a;text-align:center;padding-top:10px}
</style>
</head>
<body>

<header class="site-header">
  <div class="wrap">
    <div class="brand"><span class="brand-mark"></span><span class="brand-name">Tarnwick Growth Systems</span></div>
    <div class="signup">
      <div class="signup-input">Email Address</div>
      <div class="signup-btn">SUBSCRIBE</div>
    </div>
  </div>
</header>

<nav class="main-nav">
  <div class="wrap">
    <span class="nav-item active">HOME</span>
    <span class="nav-item">SERVICES</span>
    <span class="nav-item">ABOUT</span>
    <span class="nav-item">BLOG</span>
    <span class="nav-item">FREE TECH ASSESSMENT</span>
    <div class="nav-search"><span>Search...</span>
      <svg width="6" height="6" viewBox="0 0 10 10"><circle cx="4" cy="4" r="3" fill="none" stroke="#fff" stroke-width="1.5"/><line x1="6.3" y1="6.3" x2="9.5" y2="9.5" stroke="#fff" stroke-width="1.5"/></svg>
    </div>
  </div>
</nav>

<div class="hero" role="img" aria-label="Photo of a climber leaping between rocks above a green valley"></div>

<main class="content">
  <div class="wrap">
    <section class="blog">
      <h2 class="section-title">LATEST FROM OUR BLOG</h2>

      <article class="post">
        <div class="post-thumb t1" role="img" aria-label="Photo of a team on a snowy mountain"></div>
        <div class="post-body">
          <h3 class="post-title">Don't alienate your best customers. Oh, well, you don't know who they are?</h3>
          <p class="post-excerpt">Your best buyers leave clues in every click and order. Learn how simple data habits reveal who they are, what they value and how to keep them close without guessing.</p>
          <div class="post-meta"><span>MAY 28, 2015</span><span class="read-more">READ MORE ›</span></div>
        </div>
      </article>

      <article class="post">
        <div class="post-thumb t2" role="img" aria-label="Photo of a tablet showing a mobile website"></div>
        <div class="post-body">
          <h3 class="post-title">Are the Top 500 Brands Ready for Mobile Search?</h3>
          <p class="post-excerpt">Search on phones now leads desktop for many brands. We looked at how large firms handle speed, layout and content on small screens, and where most still fall short.</p>
          <div class="post-meta"><span>MAY 14, 2015</span><span class="read-more">READ MORE ›</span></div>
        </div>
      </article>

      <article class="post">
        <div class="post-thumb t3" role="img" aria-label="Illustration of search and analytics screens"></div>
        <div class="post-body">
          <h3 class="post-title">The Real Value of Social Likes</h3>
          <p class="post-excerpt">A like is easy to earn and easy to forget. Here is how to link social signals to real sales data so you can see which fans actually turn into customers over time.</p>
          <div class="post-meta"><span>APR 30, 2015</span><span class="read-more">READ MORE ›</span></div>
        </div>
      </article>

      <article class="post">
        <div class="post-thumb t4" role="img" aria-label="Photo of a group jumping on a beach"></div>
        <div class="post-body">
          <h3 class="post-title">Essential Strategies for Measuring Marketing Effectiveness</h3>
          <p class="post-excerpt">Clear goals, clean tracking and honest reports are the base of good measurement. Use these steps to judge each campaign and move budget to what works best.</p>
          <div class="post-meta"><span>APR 16, 2015</span><span class="read-more">READ MORE ›</span></div>
        </div>
      </article>
    </section>

    <aside class="sidebar">
      <h2 class="side-title">WHY WE ARE DIFFERENT</h2>
      <p class="side-lead">We Focus on Technology so you don't have to.</p>
      <p class="side-text">We are different from a traditional digital marketing agency in that our focus is on helping you use data, tools and systems to reach and engage your customers.</p>
      <p class="side-text">We plan, build and run the marketing technology that drives your growth, so your team can focus on the ideas and the people behind the brand.</p>
      <span class="cta">REQUEST A FREE TECH ASSESSMENT</span>

      <h2 class="side-title">RECENT POSTS</h2>
      <div class="recent">
        <div class="recent-thumb t1" role="img" aria-label="Photo of a mountain team"></div>
        <p class="recent-text">Don't alienate your best customers, you know who they are<span>May 28, 2015</span></p>
      </div>
      <div class="recent">
        <div class="recent-thumb t2" role="img" aria-label="Photo of a mobile device"></div>
        <p class="recent-text">Data points that drive a smarter campaign<span>May 14, 2015</span></p>
      </div>
      <div class="recent">
        <div class="recent-thumb t5" role="img" aria-label="Photo of an office desk"></div>
        <p class="recent-text">Five tools every growth team needs<span>Apr 30, 2015</span></p>
      </div>
    </aside>
  </div>
</main>

<section class="band">
  <div class="wrap">
    <div class="services">
      <h2 class="band-title">OUR SERVICES</h2>
      <div class="service-grid">
        <div class="service"><div class="service-thumb t3" role="img" aria-label="Photo of data dashboards"></div><p class="service-text"><b>Marketing data strategy and planning</b>We map your data to clear growth goals.</p></div>
        <div class="service"><div class="service-thumb t2" role="img" aria-label="Photo of a laptop"></div><p class="service-text"><b>Email and automation setup</b>Smart flows that keep buyers engaged.</p></div>
        <div class="service"><div class="service-thumb t4" role="img" aria-label="Photo of a team meeting"></div><p class="service-text"><b>Customer insight and analytics</b>Know who buys, why and what comes next.</p></div>
        <div class="service"><div class="service-thumb t5" role="img" aria-label="Photo of server hardware"></div><p class="service-text"><b>Technology selection and support</b>The right tools, fitted and running well.</p></div>
      </div>
    </div>
    <div class="tweets">
      <h2 class="band-title">TWEETS</h2>
      <div class="tweet"><span class="tweet-icon"></span><p class="tweet-text"><span>@tarnwickgrowth</span> New post on measuring what matters in your next campaign. <em>2 hours ago</em></p></div>
      <div class="tweet"><span class="tweet-icon"></span><p class="tweet-text"><span>@tarnwickgrowth</span> Mobile search keeps climbing. Is your site ready for it? <em>1 day ago</em></p></div>
      <div class="tweet"><span class="tweet-icon"></span><p class="tweet-text"><span>@tarnwickgrowth</span> Clean data beats big data. Start with what you already own. <em>3 days ago</em></p></div>
      <div class="tweet"><span class="tweet-icon"></span><p class="tweet-text"><span>@tarnwickgrowth</span> Book a free tech assessment with our team this month. <em>5 days ago</em></p></div>
    </div>
  </div>
</section>

<footer class="site-footer">
  <div class="wrap">
    <div class="foot-brand">
      <span class="brand-name">Tarnwick Growth Systems</span>
      <p>Data driven marketing technology that helps you reach and keep customers.</p>
    </div>
    <div class="foot-links">
      <div class="foot-col">Home<br>Sign in<br>Join<br>Contact us</div>
      <div class="foot-col">Our services<br>Data strategy<br>Email setup<br>Analytics</div>
      <div class="foot-col">About us<br>Careers<br>Privacy</div>
    </div>
    <div class="social">
      <div class="social-title">SOCIAL NETWORK</div>
      <div class="social-row">
        <span class="social-dot"></span>
        <span class="social-dot"></span>
        <span class="social-dot"></span>
        <span class="social-dot accent"></span>
      </div>
    </div>
  </div>
  <div class="copyright">Copyright 2015 Tarnwick Growth Systems LLC. All rights reserved.</div>
</footer>

</body>
</html>
```